Business card for job seeker professional

Hi. I'm a sale and marketing professional who's just moved to Australia and looking for a job. I would like to have a business card designed for me, which I can use for job interviews/networking. Given Pravolink increasing importance in the job market, I would like my public profile link (http://au.pravolink-net.com/in/tomasveridun/) to be incorporated into my details.

```html
<!DOCTYPE html>
<html lang="en">
<head>
<meta charset="utf-8">
<title>Tomas Veridun – Business Card</title>
<link rel="stylesheet" href="https://fonts.googleapis.com/css2?family=Source+Sans+3:wght@400;600;700&display=swap">
<style>
  :root {
    --backdrop: #e7e8ea;
    --card-green: #9dbf51;
    --brand-blue: #0e75b6;
    --name-blue: #1170b3;
    --paper: #ffffff;
    --ink: #111111;
    --shadow: rgba(0, 0, 0, 0.45);
  }
  html, body {
    margin: 0;
    padding: 0;
    overflow: hidden;
  }
  body {
    width: 1200px;
    height: 1000px;
    background: var(--backdrop);
    position: relative;
    font-family: "Source Sans 3", "Myriad Pro", Arial, sans-serif;
  }
  .card {
    position: absolute;
    width: 734px;
    height: 423px;
    border-radius: 30px;
    overflow: hidden;
    box-shadow: 6px 7px 7px var(--shadow);
  }
  .card--front {
    left: 64px;
    top: 49px;
    background: var(--card-green);
  }
  .card--back {
    left: 402px;
    top: 527px;
    background: var(--paper);
  }
  .holder {
    position: absolute;
    left: 44px;
    top: 243px;
  }
  .holder__name {
    margin: 0 0 9px;
    font-size: 51px;
    font-weight: 700;
    line-height: 1;
    color: var(--name-blue);
    letter-spacing: 0.3px;
  }
  .holder__skills {
    list-style: none;
    margin: 0;
    padding: 0;
    color: var(--paper);
    font-size: 22px;
    font-weight: 600;
    line-height: 27.5px;
    letter-spacing: 0.35px;
  }
  .back__band {
    position: absolute;
    left: 0;
    top: 0;
    width: 100%;
    height: 265px;
    background: var(--brand-blue);
  }
  .contact {
    position: absolute;
    left: 44px;
    top: 274px;
    margin: 0;
    padding: 0;
    list-style: none;
    color: var(--ink);
    font-size: 22px;
    line-height: 38px;
    letter-spacing: 0.2px;
  }
  .contact__label {
    font-weight: 700;
  }
  .contact__url {
    font-weight: 700;
  }
</style>
</head>
<body>
  <section class="card card--front" aria-label="Card front">
    <div class="holder">
      <h1 class="holder__name">Tomas Veridun</h1>
      <ul class="holder__skills">
        <li>Business Strategy</li>
        <li>International Business Development</li>
        <li>Marketing and Communication</li>
      </ul>
    </div>
  </section>

  <section class="card card--back" aria-label="Card back">
    <div class="back__band"></div>
    <ul class="contact">
      <li><span class="contact__label">Email</span> example-mail@examplesite.com</li>
      <li><span class="contact__label">Mobile Number</span> 0000 000 000</li>
      <li><span class="contact__label">Pravolink</span> <span class="contact__url">http://au.pravolink-net.com/in/tomasveridun/</span></li>
    </ul>
  </section>
</body>
</html>
```